New website for Holloway Law Firm at www.keepfirmplan.example

We are a professional law firm located in the Nashville, Tennessee USA area. We focus on personal injury law. We are looking for a slick new website that is user friendly for updating with new blogs, videos, etc. The primary colors should be red, black, and white. It should load extremely fast and have a good mobile component. The pages for the design will include a home page, about us, news, contact us, and practice page. The practice page will be copied for all the practice areas including motor vehicle accidents, slip and fall accidents, dog bites, etc. We have included an image which we would like to include in the new site which shows the color scheme The image is called banner-Car Wreck. The new website should NOT have gavels, court houses, law books, scales or the typical images for a law firm.

Target Market(s)

People in Tennessee involved in accidents

Industry/Entity Type

Legal services, law firm

Number of Pages Required

5+ page

Font styles to use
Serif

Colors
EB3D1F
EC4F4E
F09395
F8D3D4
FCEDEE

Requirements
Should not have
• Gavels, columns, scales, law related images

```html
<!DOCTYPE html>
<html lang="en">
<head>
<meta charset="utf-8">
<title>Personal Injury | Holloway Law Firm</title>
<link rel="stylesheet" href="https://fonts.googleapis.com/css2?family=Playfair+Display:wght@700;900&family=Montserrat:wght@400;500;600;800&display=swap">
<style>
:root{
  --ink:#181c23;
  --red:#c32026;
  --white:#ffffff;
  --paper:#f3f3f3;
  --text:#3b3f46;
  --muted:#7c7f85;
  --rule:#c9c9c9;
  --serif:'Playfair Display', Georgia, serif;
  --sans:'Montserrat', Arial, sans-serif;
}
*{margin:0;padding:0;box-sizing:border-box}
html,body{width:1200px;height:2228px;overflow:hidden;background:var(--white)}
body{position:relative;font-family:var(--sans);color:var(--text)}
.abs{position:absolute}

.hero-panel{left:656px;top:0;width:544px;height:396px;background:var(--ink)}
.hero-photo{left:0;top:0;width:773px;height:443px;background:linear-gradient(135deg,#3b4a5c 0%,#8a96a3 45%,#c9b9a4 70%,#4a5565 100%)}
.brand{font-family:var(--serif);font-weight:700;white-space:nowrap}
.brand-head{left:89px;top:34px;font-size:22px;color:var(--white)}
.nav{left:700px;top:36px;display:flex;gap:22px;font-size:13.5px;font-weight:500;color:var(--white)}
.call-btn{left:1066px;top:24px;width:44px;height:41px;background:var(--red);display:flex;align-items:center;justify-content:center}
.hero-title{left:740px;top:142px;font-family:var(--serif);font-weight:900;font-size:82px;line-height:66px;letter-spacing:1px}
.hero-title span{display:block}
.hero-title .w{color:var(--white)}
.hero-title .r{color:var(--red)}

.intro-bar{left:89px;top:536px;width:3px;height:80px;background:var(--red)}
.eyebrow{left:109px;top:541px;font-size:14px;font-weight:600;letter-spacing:3px;color:var(--ink)}
.intro-title{left:109px;top:553px;font-family:var(--serif);font-weight:700;font-size:48px;color:var(--ink);letter-spacing:1px}
.copy{left:89px;top:640px;width:540px;font-size:12.6px;line-height:19.5px}
.copy p{margin-bottom:30px}
.side-photo{left:655px;top:501px;width:456px;height:585px;background:linear-gradient(160deg,#cfd3d6 0%,#7d8690 40%,#2a2f38 60%,#8c9096 100%)}

.chat{left:89px;top:1182px;width:1026px;height:667px;background:var(--paper)}
.chat-title{left:0;top:1236px;width:1200px;text-align:center;font-family:var(--serif);font-weight:700;font-size:50px;color:var(--ink);letter-spacing:1px}
.chat-lede{left:306px;top:1316px;width:588px;text-align:center;font-size:12.6px;line-height:19.5px;color:var(--muted)}
.field{border-bottom:1px solid var(--rule);font-size:11.5px;color:var(--muted);padding-left:2px}
.f-first{left:285px;top:1460px;width:297px;height:36px}
.f-last{left:618px;top:1460px;width:297px;height:36px}
.f-email{left:285px;top:1522px;width:630px;height:36px}
.f-help{left:285px;top:1585px;width:630px;height:53px}
.submit{left:524px;top:1668px;width:152px;height:33px;background:var(--red);color:var(--white);font-size:12px;font-weight:800;letter-spacing:3px;display:flex;align-items:center;justify-content:center}
.disclaimer{left:360px;top:1727px;width:480px;text-align:center;font-size:7.5px;line-height:11.5px;color:#9a9a9a}

.footer{left:0;top:1917px;width:1200px;height:311px;background:var(--ink)}
.brand-foot{left:89px;top:1982px;font-size:32px;color:var(--red)}
.foot-head{font-size:19px;font-weight:800;color:var(--white);letter-spacing:-.3px}
.foot-list{list-style:none;font-size:12px;font-weight:500;color:var(--white);line-height:22.5px}
.contact-list li{display:flex;align-items:flex-start;gap:9px;margin-bottom:4px}
.contact-list svg{flex:none;margin-top:4px}
.social{left:908px;top:2024px;display:flex;gap:12px}
.social span{width:24px;height:24px;border-radius:50%;background:var(--white)}
.foot-rule{left:89px;top:2175px;width:1022px;height:1px;background:#4a4e56}
.copyright{left:0;top:2195px;width:1200px;text-align:center;font-size:11px;color:var(--white)}
</style>
</head>
<body>
<div class="abs hero-panel"></div>
<div class="abs hero-photo" role="img" aria-label="Photo of a team of colleagues gathered around a table reviewing documents"></div>
<div class="abs brand brand-head">Holloway Law Firm</div>
<nav class="abs nav"><span>Home</span><span>About us</span><span>News</span><span>Contact us</span><span>Practice</span></nav>
<div class="abs call-btn"><svg width="16" height="16" viewBox="0 0 24 24" aria-label="Call"><path fill="#fff" d="M6.6 10.8a15.1 15.1 0 0 0 6.6 6.6l2.2-2.2c.3-.3.7-.4 1-.2 1.1.4 2.3.6 3.6.6.6 0 1 .4 1 1V20c0 .6-.4 1-1 1C10.6 21 3 13.4 3 4c0-.6.4-1 1-1h3.5c.6 0 1 .4 1 1 0 1.3.2 2.5.6 3.6.1.3 0 .7-.2 1z"/></svg></div>
<h1 class="abs hero-title"><span class="w">Personal</span><span class="r">Injury</span></h1>

<div class="abs intro-bar"></div>
<div class="abs eyebrow">PRACTICES</div>
<h2 class="abs intro-title">Personal Injury</h2>
<div class="abs copy">
<p>Our personal injury clients don’t ask to be involved in these types of cases. They don’t ask to be hit by a car, rear ended by a semi, or become the victim of a negligent doctor, and they certainly don’t ask for the pain that follows. Our clients are normal every day people who were in the wrong place at the wrong time. Since 2005, we have helped recover millions of dollars from insurance companies to compensate our clients for what they have lost.</p>
<p>Insurance companies love to make offers which are low and early. Immediately after a wreck, a car wreck victim may be contacted by an adjuster who acts like they care and want what is best for the victim when in-fact they are simply trying to meet their quarterly bonus based upon the amounts paid. What the poor victim doesn’t understand is that they must pay for their past, present and future medical bills out of the settlement and they must reimburse their own health insurance company for those expenses. Sadly, we have been contacted by numerous personal injury victims who settled with the insurance company too soon and now they can’t make a living because the settlement wasn’t enough.</p>
<p>Whether a personal injury victim hires the Holloway Law Firm or another attorney, they are increasing their chances of survival against the insurance companies. If you are victim of personal injury or you are close to someone who was a victim, please contact an attorney today. We do not charge a dime unless and until you are compensated for your injury. That is why our motto is “Don’t Lose what’s Legally Your’s”. Don’t lose the money from the insurance company which is legally your’s!</p>
</div>
<div class="abs side-photo" role="img" aria-label="Photo of an injured woman sitting on the road beside a car after a collision"></div>

<section class="abs chat"></section>
<h2 class="abs chat-title">Let's Chat.</h2>
<p class="abs chat-lede">Use the form below to contact us regarding your legal inquiry. Please be as detailed as possible. Include the facts of your case and who is involved. To help us best service you, we recommend that you first describe the issue you’re having before telling us what you want to achieve. You may also email or call us to make an appointment.</p>
<div class="abs field f-first">First Name *</div>
<div class="abs field f-last">Last&nbsp; Name *</div>
<div class="abs field f-email">Email Address *</div>
<div class="abs field f-help">How Can We Help? *</div>
<div class="abs submit">SUBMIT</div>
<p class="abs disclaimer">Please do not include confidential or sensitive information in your message. In the event that we are representing a party with opposing interests to your own, we may have a duty to disclose any information you provide to our client.</p>

<footer class="abs footer"></footer>
<div class="abs brand brand-foot">Holloway Law Firm</div>
<div class="abs foot-head" style="left:395px;top:1978px">QUICK LINKS</div>
<ul class="abs foot-list" style="left:396px;top:2012px"><li>Home</li><li>About us</li><li>News</li><li>Contact us</li><li>Practice</li></ul>
<div class="abs foot-head" style="left:596px;top:1978px">CONTACT US</div>
<ul class="abs foot-list contact-list" style="left:596px;top:2012px;width:260px">
<li><svg width="11" height="13" viewBox="0 0 24 28"><path fill="#fff" d="M12 0a10 10 0 0 0-10 10c0 7.5 10 18 10 18s10-10.5 10-18A10 10 0 0 0 12 0zm0 14a4 4 0 1 1 0-8 4 4 0 0 1 0 8z"/></svg><span>1840 Maple Ridge Road | Suite 210<br>| Franklin, TN 37064</span></li>
<li><svg width="13" height="13" viewBox="0 0 24 24"><path fill="#fff" d="M6.6 10.8a15.1 15.1 0 0 0 6.6 6.6l2.2-2.2c.3-.3.7-.4 1-.2 1.1.4 2.3.6 3.6.6.6 0 1 .4 1 1V20c0 .6-.4 1-1 1C10.6 21 3 13.4 3 4c0-.6.4-1 1-1h3.5c.6 0 1 .4 1 1 0 1.3.2 2.5.6 3.6.1.3 0 .7-.2 1z"/></svg><span>Phone: (615) 555-0142</span></li>
<li><svg width="13" height="11" viewBox="0 0 24 18"><path fill="#fff" d="M0 0h24v2L12 10 0 2zM0 4l12 8 12-8v14H0z"/></svg><span>Email: office@hollowaylawfirm.example</span></li>
</ul>
<div class="abs foot-head" style="left:908px;top:1978px">SOCIAL</div>
<div class="abs social" aria-label="Social profiles"><span></span><span></span><span></span><span></span></div>
<div class="abs foot-rule"></div>
<div class="abs copyright">©2021 Holloway Law Firm, PLLC.&nbsp; All Rights Reserved.</div>
</body>
</html>
```